VARLEX CONSULTING / PROJECT MANAGEMENT WEB DESIGN

Design Brief: Varlex Consulting Website

I own 'VARLEX' business name and therefore can keep the name and logo simple i.e. VARLEX only and incorporate consulting / Project Management within the design or text.

Purpose:

The purpose of this project is to create a website for Varlex.com.au, a project management consulting company. The website will promote the company's services, allowing potential clients to learn more about Varlex and its capabilities. The website should be professional, easy to navigate, and provide all necessary information for potential clients.

Target Audience:

Clients in the Oil & Gas, LNG, and Chemical industry
Businesses and organizations in need of project management and engineering consultancy services
Potential clients looking for information about the company and its services
Key Elements:
Clean and modern design that reflects the company's professional image and incorporates the company logo

Clear and easy-to-use navigation menu

“Homepage” that promotes the company's main services and includes the company's mission statement.

Services:

PROJECT MANAGEMENT
PROJECT ENGINEERING
QUALITY MANAGEMENT AND PROCESS DEVELOPMENT
BUSINESS CASE DEVELOPMENT
ENGINEERING & DESIGN MANAGEMENT
CONCEPT STUDIES AND PROJECT SUPPORT
CONSTRUCTION MANAGEMENT
CONTRACT MANAGEMENT / CLAIMS PROCUREMENT / SUPPLY CHAIN SUPPORT
COMMERCIAL LIABILITY & RISK MANAGEMENT

Mission Statement:

"Our mission at Varlex is to provide expert project management and engineering consultancy services that help our clients achieve their goals and exceed their expectations. We will accomplish this by offering a full range of services, providing experienced and highly-qualified professionals, building strong relationships with our clients, continuously improving our services, and maintaining a reputation for excellence."

"About" page that includes client-supplied text about the company
"Contact" page with an editable form, email, and phone number for potential clients to get in touch with the company

Design Style:

Professional and modern
Clean and simple layout
Use of the company's colors and branding (subject to change)
Use of high-quality images that reflect the industry and services

Functionality:
Responsive design that is optimized for all devices and screen sizes

Website will be coded and uploaded to a content management system (CMS) for easy updates and maintenance
Website will be optimized for search engines and include all necessary SEO elements
Website will be fully tested for compatibility with all modern web browsers and devices
Website will be secured with an SSL certificate to ensure the safety of user data (client hosting includes SSL certificate).

Target Market(s)

Clients in the Oil & Gas, LNG, and Chemical industry Businesses and organizations in need of project management and engineering consultancy services Potential clients looking for information about the company and its services

Industry/Entity Type

Oil & Gas, LNG, and Chemical industry Businesses and organizations

Coding

Coded - Design and coding required

Number of Pages Required

3 page

Font styles to use
Sans Serif

Colors
0054AA
0677BA
7BADD7
CADEEF
E8F1F8
EB3D1F
EC4F4E
F09395
F8D3D4
FCEDEE
6B429C
8869AF
B7A5CE
E3DAEB
F3F0F8

Requirements
Must have
• HOME ABOUT AND CONTACT PAGE
Nice to have
• Fresh look, open to ideas
Should not have
• Stock images and hand shakes and meeting rooms..

```html
<!DOCTYPE html>
<html lang="en">
<head>
<meta charset="utf-8">
<title>Varlex Resources — Project Management Consulting</title>
<link href="https://fonts.googleapis.com/css2?family=Montserrat:wght@500;600;700;800&family=Poppins:wght@400;500;600&display=swap" rel="stylesheet">
<style>
:root{
  --blue:#2ea3f2;
  --blue-deep:#1a8fe6;
  --blue-soft:#eef6fd;
  --ink:#1b1b1b;
  --text:#444;
  --dark:#232427;
  --white:#fff;
}
*{box-sizing:border-box;margin:0;padding:0}
html,body{width:1200px;height:4003px;overflow:hidden;background:var(--white)}
body{position:relative;font-family:"Poppins",sans-serif;color:var(--text)}
.abs{position:absolute}
h1,h2,h3,.nav,.btn{font-family:"Montserrat",sans-serif}

/* header */
.site-header{left:0;top:0;width:1200px;height:124px;background:var(--white);z-index:5}
.brand-tab{left:120px;top:0;width:292px;height:146px;background:var(--white);border-radius:0 0 40px 40px;z-index:6;display:flex;flex-direction:column;align-items:center;justify-content:center;gap:10px}
.brand-dot{width:22px;height:22px;border-radius:50%;background:var(--blue)}
.brand-name{font-family:"Montserrat",sans-serif;font-weight:700;font-size:23px;color:var(--blue);letter-spacing:.3px}
.call{right:152px;top:22px;font-family:"Montserrat",sans-serif;font-weight:700;font-size:17px;color:var(--blue);display:flex;align-items:center;gap:8px}
.nav{right:150px;top:72px;display:flex;gap:58px;font-weight:600;font-size:15px;color:var(--ink)}
.nav .active{color:var(--blue)}

/* hero */
.hero-photo{left:0;top:124px;width:1200px;height:770px;background:linear-gradient(120deg,#3b4756 0%,#6f7f8f 35%,#9fb4c6 60%,#c9d8e4 100%)}
.hero-waves{left:0;top:480px;width:1200px;height:420px}
.hero-brand{left:780px;top:310px;font-family:"Montserrat",sans-serif;font-weight:700;font-size:32px;color:var(--blue-deep)}
.hero-title{left:600px;top:508px;width:560px;text-align:center;font-weight:800;font-size:46px;line-height:46px;color:var(--white)}
.btn{display:flex;align-items:center;justify-content:center;background:var(--blue);color:var(--white);font-weight:700;font-size:16px;border-radius:0 18px 0 18px}
.hero-btn{left:810px;top:620px;width:150px;height:46px}

/* services */
.services-title{left:181px;top:895px;font-weight:700;font-size:44px;color:var(--ink)}
.services-intro{left:184px;top:960px;width:480px;font-size:16px;line-height:22px;color:var(--ink)}
.services-grid{left:181px;top:1055px;display:grid;grid-template-columns:repeat(3,262px);grid-auto-rows:242px;gap:27px 26px}
.service-card{background:var(--blue-soft);border-radius:10px 70px 10px 10px;display:flex;flex-direction:column;align-items:center;text-align:center;padding-top:34px;color:var(--ink)}
.service-card.active{background:var(--blue);color:var(--white)}
.service-card svg{width:62px;height:62px;margin-bottom:16px}
.service-card h3{font-weight:500;font-size:14px;line-height:21px;height:64px;text-transform:uppercase}
.service-card .more{font-size:11px;margin-top:6px}
.service-card .more::after{content:"";display:inline-block;width:6px;height:6px;border-radius:50%;background:var(--blue);margin-left:4px;vertical-align:middle}
.service-card.active .more::after{background:var(--white)}

/* mission */
.mission-band{left:0;top:1930px;width:1200px;height:680px}
.mission-title{left:145px;top:2102px;font-weight:700;font-size:40px;color:var(--white)}
.mission-text{left:149px;top:2175px;width:510px;font-size:19px;line-height:28px;color:var(--white)}

/* about */
.about-frame{left:197px;top:2633px;width:348px;height:424px;border:2px solid var(--blue);border-radius:0 130px 0 0}
.about-dot{left:114px;top:2993px;width:94px;height:94px;border-radius:50%;background:var(--blue)}
.about-photo{left:156px;top:2695px;width:346px;height:422px;border-radius:0 130px 0 130px;background:linear-gradient(135deg,#c9ced4,#8d96a0 55%,#5e6a78)}
.about-title{left:578px;top:2694px;font-weight:700;font-size:46px;color:var(--ink)}
.about-text{left:580px;top:2772px;width:480px;font-size:15.5px;line-height:21.4px;color:#555}
.about-btn{left:589px;top:3058px;width:150px;height:46px}

/* footer */
.footer-shape{left:0;top:3240px;width:1200px;height:763px}
.contact-title{left:153px;top:3495px;font-weight:700;font-size:38px;color:var(--white)}
.field{background:var(--white);height:48px;font-size:13px;color:#777;display:flex;align-items:center;padding-left:14px;gap:6px}
.field.message{align-items:flex-start;padding-top:14px;height:102px}
.submit{left:156px;top:3813px;width:122px;height:45px;font-size:15px}
.info{left:716px;top:3572px;width:340px;color:var(--white);font-size:15px;line-height:22px}
.info h4{font-family:"Montserrat",sans-serif;color:var(--blue);font-size:17px;font-weight:700;display:flex;align-items:center;gap:8px;margin-bottom:6px}
.info p{margin-bottom:30px}
.socials{left:158px;top:3935px;display:flex;gap:16px}
.socials span{width:20px;height:20px;border-radius:50%;background:var(--blue)}
.copyright{left:694px;top:3928px;font-size:12px;color:var(--white)}
</style>
</head>
<body>

<header class="site-header abs">
  <div class="call abs">
    <svg width="20" height="20" viewBox="0 0 20 20"><circle cx="10" cy="10" r="10" fill="#2ea3f2"/><path d="M7 5l2 2-1 1.5c.6 1.3 1.6 2.3 2.9 2.9L12.4 10l2 2-1.3 1.7C9.6 13.4 6.6 10.4 6.3 6.8z" fill="#fff"/></svg>
    CALL US: 555 010 2468
  </div>
  <nav class="nav abs"><span class="active">HOME</span><span>ABOUT</span><span>SERVICES</span><span>CONTACT</span></nav>
</header>
<div class="brand-tab abs"><span class="brand-dot"></span><span class="brand-name">VARLEX RESOURCES</span></div>

<section class="hero">
  <div class="hero-photo abs" role="img" aria-label="Consultants working together in a bright glass-walled office"></div>
  <div class="hero-brand abs">VARLEX RESOURCES</div>
  <h1 class="hero-title abs">WELCOME TO<br>VARLEX RESOURCES</h1>
  <div class="btn hero-btn abs">READ MORE</div>
  <svg class="hero-waves abs" viewBox="0 0 1200 420" preserveAspectRatio="none">
    <path d="M0 68 C200 160 420 330 760 330 C980 330 1120 250 1200 180 L1200 420 L0 420Z" fill="#fff"/>
    <path d="M330 200 C560 360 880 410 1200 232 L1200 262 C900 430 560 390 330 200Z" fill="#2ea3f2"/>
    <path d="M470 250 C700 360 960 380 1200 272 L1200 286 C960 400 700 380 470 250Z" fill="#2ea3f2"/>
  </svg>
</section>

<section class="services">
  <h2 class="services-title abs">VARLEX SERVICES</h2>
  <p class="services-intro abs">Lorem ipsum dolor sit amet, consectetur adipiscing elit, sed do eiusmod tempor incididunt ut labore et dolore.</p>
  <div class="services-grid abs">
    <div class="service-card"><svg viewBox="0 0 62 62" fill="none" stroke="#2ea3f2" stroke-width="2"><circle cx="31" cy="31" r="14"/><circle cx="31" cy="31" r="6"/><path d="M31 10v6M31 46v6M10 31h6M46 31h6"/></svg><h3>Project<br>Management</h3><span class="more">Read More</span></div>
    <div class="service-card active"><svg viewBox="0 0 62 62" fill="none" stroke="#fff" stroke-width="2"><circle cx="31" cy="24" r="10"/><path d="M14 54c0-10 8-16 17-16s17 6 17 16"/><path d="M19 22h24"/></svg><h3>Project<br>Engineering</h3><span class="more">Read More</span></div>
    <div class="service-card"><svg viewBox="0 0 62 62" fill="none" stroke="#2ea3f2" stroke-width="2"><path d="M12 42l14-18 10 8 14-16"/><path d="M31 4v6M20 8l3 5M42 8l-3 5"/></svg><h3>Quality Management<br>and Process Development</h3><span class="more">Read More</span></div>
    <div class="service-card"><svg viewBox="0 0 62 62" fill="none" stroke="#2ea3f2" stroke-width="2"><circle cx="31" cy="31" r="20"/><circle cx="31" cy="31" r="12"/><path d="M25 31l4 4 8-8"/></svg><h3>Business Case<br>Development</h3><span class="more">Read More</span></div>
    <div class="service-card"><svg viewBox="0 0 62 62" fill="none" stroke="#2ea3f2" stroke-width="2"><circle cx="24" cy="28" r="9"/><path d="M10 56c0-9 6-14 14-14s14 5 14 14"/><circle cx="44" cy="16" r="7"/><path d="M44 4v2M54 16h2"/></svg><h3>Engineering &amp;<br>Design Management</h3><span class="more">Read More</span></div>
    <div class="service-card"><svg viewBox="0 0 62 62" fill="none" stroke="#2ea3f2" stroke-width="2"><circle cx="33" cy="20" r="10"/><path d="M18 54c0-10 7-16 15-16s15 6 15 16"/><path d="M10 36l8 8"/></svg><h3>Concept Studies<br>and Project Support</h3><span class="more">Read More</span></div>
    <div class="service-card"><svg viewBox="0 0 62 62" fill="none" stroke="#2ea3f2" stroke-width="2"><path d="M20 22a11 11 0 0 1 22 0z"/><circle cx="31" cy="30" r="8"/><path d="M16 56c0-10 7-16 15-16s15 6 15 16"/></svg><h3>Construction<br>Management</h3><span class="more">Read More</span></div>
    <div class="service-card"><svg viewBox="0 0 62 62" fill="none" stroke="#2ea3f2" stroke-width="2"><path d="M31 8l20 11v24L31 54 11 43V19z"/><path d="M11 19l20 11 20-11M31 30v24"/></svg><h3>Contract Management /<br>Claims Procurement /<br>Supply Chain Support</h3><span class="more">Read More</span></div>
    <div class="service-card"><svg viewBox="0 0 62 62" fill="none" stroke="#2ea3f2" stroke-width="2"><path d="M22 10l16 6v14c0 12-8 18-16 22-8-4-16-10-16-22V16z"/><circle cx="44" cy="18" r="6"/><path d="M38 54c0-10 3-16 6-16s6 6 6 16"/></svg><h3>Commercial Liability<br>&amp; Risk Management</h3><span class="more">Read More</span></div>
  </div>
</section>

<section class="mission">
  <svg class="mission-band abs" viewBox="0 0 1200 680" preserveAspectRatio="none">
    <defs><radialGradient id="missionGlow" cx="0.78" cy="0.45" r="0.4"><stop offset="0" stop-color="#ffffff" stop-opacity=".55"/><stop offset="1" stop-color="#ffffff" stop-opacity="0"/></radialGradient></defs>
    <path d="M0 85 L1080 10 Q1200 0 1200 120 L1200 560 Q1200 670 1090 670 L0 570Z" fill="#2ea3f2"/>
    <path d="M0 85 L1080 10 Q1200 0 1200 120 L1200 560 Q1200 670 1090 670 L0 570Z" fill="url(#missionGlow)"/>
  </svg>
  <h2 class="mission-title abs">MISSION STATEMENT</h2>
  <p class="mission-text abs">Our mission at Varlex is to provide expert project management and engineering consultancy services that help our clients achieve their goals and exceed their expectations. We will accomplish this by offering a full range of services, providing experienced and highly-qualified professionals, building strong relationships with our clients, continuously improving our services, and maintaining a reputation for excellence."</p>
</section>

<section class="about">
  <div class="about-frame abs"></div>
  <div class="about-dot abs"></div>
  <div class="about-photo abs" role="img" aria-label="Smiling consultant in a grey suit greeting a client"></div>
  <h2 class="about-title abs">ABOUT ME</h2>
  <p class="about-text abs">Sed ut perspiciatis unde omnis iste natus error sit voluptatm accusantium doloremque laudantium, totam rem aperiam, eaque ipsa quae ab illo inventore veritatis et quasi archiecto beatae vitae dicta sunt explicabo. Nemo enim ipsaloreishm voluptatem quia voluptas sit aspernatur aut odit aut fugit, sed quia consequuntur magni dolores eos qui ratione volup tatem sequi nesciunt. Neque porro quisquam est, qui dolore mpsum quia dolor sit amet, consectetur, adipisci velit, sed quia non numquam eius modi tempora incidunt ut labore et dolore magnam aliquam quaerat voluptatem. Ut enim ad minima veniam, quis nostrum exercitationem ullam corporis suscipit laboriosam.</p>
  <div class="btn about-btn abs">READ MORE</div>
</section>

<footer class="contact">
  <svg class="footer-shape abs" viewBox="0 0 1200 763" preserveAspectRatio="none">
    <path d="M0 160 C220 40 520 20 720 110 C880 180 1020 160 1200 120 L1200 763 L0 763Z" fill="#2ea3f2"/>
    <path d="M0 205 C230 80 520 70 740 170 C880 235 1040 235 1200 220 L1200 763 L0 763Z" fill="#fff"/>
    <path d="M0 250 C230 120 520 110 740 210 C880 275 1040 275 1200 260 L1200 763 L0 763Z" fill="#2ea3f2"/>
    <path d="M0 300 C260 170 560 200 800 300 C960 365 1080 365 1200 350 L1200 763 L0 763Z" fill="#232427"/>
  </svg>
  <h2 class="contact-title abs">CONTACT US</h2>
  <div class="field abs" style="left:156px;top:3565px;width:248px">&#128100;&#xFE0E; First Name</div>
  <div class="field abs" style="left:420px;top:3565px;width:248px">&#128100;&#xFE0E; Last Name</div>
  <div class="field abs" style="left:156px;top:3631px;width:248px">&#9993;&#xFE0E; Email</div>
  <div class="field abs" style="left:420px;top:3631px;width:248px">&#9990;&#xFE0E; Phone</div>
  <div class="field message abs" style="left:156px;top:3697px;width:512px">&#9998;&#xFE0E; Message</div>
  <div class="btn submit abs">SUBMIT</div>
  <div class="info abs">
    <h4><svg width="14" height="18" viewBox="0 0 14 18"><path d="M7 0a7 7 0 0 1 7 7c0 5-7 11-7 11S0 12 0 7a7 7 0 0 1 7-7z" fill="#2ea3f2"/><circle cx="7" cy="7" r="2.5" fill="#232427"/></svg>ADDRESS</h4>
    <p>4127 Bellmora Parade, Ste. 208<br>Westhaven Au 61090</p>
    <h4><svg width="16" height="16" viewBox="0 0 16 16"><path d="M3 1l3 3-1.5 2c.8 1.8 2.2 3.2 4 4L10.5 8.5l3 3-2 2.5C6 13.5 2.5 10 1 3z" fill="#2ea3f2"/></svg>PHONE</h4>
    <p>Ph: 000-555-0187</p>
    <h4><svg width="17" height="13" viewBox="0 0 17 13"><rect width="17" height="13" rx="1.5" fill="#2ea3f2"/><path d="M1 1l7.5 6L16 1" stroke="#232427" fill="none" stroke-width="1.5"/></svg>EMAIL</h4>
    <p>Email:hello@varlexmail.com</p>
  </div>
  <div class="socials abs" aria-label="Social links"><span></span><span></span><span></span><span></span></div>
  <p class="copyright abs">Copyright© 2023 VARLEX CONSULTING. All Rights Reserved.</p>
</footer>

</body>
</html>
```